Professional Photography Business cards

I need business cards that include my logo which I have uploaded. I run a photography business. I am open to ideas but I would like one side to have my logo and the other side to have my contact info. I don't have a website made but I do own a website domain. I have uploaded 2 different logo color schemes. My business colors are Blue, black , and white.

Business Name
Business Phone Number
Business Email
Business Website address
Instagram

Industry/Entity Type

Professional Photography

Contact Information for Business Card

Phone Number: 555-304-7826 email: info@tkale-studio.example Instagram: @t.kalestudio website doman- www.tkale-studio.example

Requirements
Must have
• I like the idea of a business card with a full black background front and back of card. My colors must include royal blue, black, and white

```html
<!DOCTYPE html>
<html lang="en">
<head>
<meta charset="utf-8">
<title>T. Kale Photography – Business Card</title>
<link href="https://fonts.googleapis.com/css2?family=Oswald:wght@600&family=Montserrat:wght@400;500&display=swap" rel="stylesheet">
<style>
  :root {
    --backdrop: #d2d3ce;
    --paper: #f3f3f1;
    --ink: #1f1f1f;
    --royal-blue: #1f1fa8;
    --edge-blue: #3a3fc0;
    --card-black: #1e1e1e;
    --emboss: #3a3a3a;
  }
  * { margin: 0; padding: 0; box-sizing: border-box; }
  html, body {
    width: 1200px; height: 1058px; overflow: hidden;
    background: var(--backdrop);
  }
  .sheet {
    width: 1200px; height: 1058px;
    display: flex; align-items: center; justify-content: center; gap: 44px;
  }
  .card {
    width: 530px; height: 303px;
    border-bottom: 4px solid var(--edge-blue);
    position: relative;
  }
  .card--front {
    background: var(--paper);
    display: flex; align-items: center; justify-content: center; gap: 26px;
    padding-left: 40px;
  }
  .identity { text-align: right; }
  .identity__name {
    font-family: "Oswald", sans-serif; font-weight: 600;
    font-size: 34px; letter-spacing: 1px; text-transform: uppercase;
    color: var(--royal-blue); line-height: 1.05;
  }
  .identity__role {
    font-family: "Montserrat", sans-serif; font-size: 15px;
    color: var(--ink); margin-top: 2px;
  }
  .divider { width: 1.5px; height: 72px; background: var(--royal-blue); }
  .contact { list-style: none; }
  .contact__item {
    display: flex; align-items: center; gap: 7px;
    font-family: "Montserrat", sans-serif; font-size: 13.5px;
    color: var(--ink); line-height: 1.55;
  }
  .contact__icon { width: 9px; height: 9px; flex: none; }
  .card--back {
    background: var(--card-black);
    display: flex; align-items: center; justify-content: center; gap: 14px;
  }
  .wordmark__dot {
    width: 38px; height: 38px; border-radius: 50%;
    border: 2px solid var(--emboss);
  }
  .wordmark__name {
    font-family: "Montserrat", sans-serif; font-weight: 500;
    font-size: 26px; letter-spacing: 3px; color: var(--emboss);
  }
</style>
</head>
<body>
<main class="sheet">
  <section class="card card--front" aria-label="Contact side">
    <div class="identity">
      <h1 class="identity__name">Tomas Kale</h1>
      <p class="identity__role">Founder</p>
    </div>
    <div class="divider"></div>
    <ul class="contact">
      <li class="contact__item">
        <svg class="contact__icon" viewBox="0 0 10 10"><path d="M2 1 L4 1 L4.5 3 L3.3 4 Q4.5 6.2 6 6.8 L7 5.6 L9 6 L9 8 Q8 9.3 6 8.6 Q2 7 1.2 3 Q1 1.6 2 1Z" fill="var(--royal-blue)"/></svg>
        555-304-7826
      </li>
      <li class="contact__item">
        <svg class="contact__icon" viewBox="0 0 10 10"><rect x="0.7" y="1.7" width="8.6" height="6.6" fill="none" stroke="var(--royal-blue)" stroke-width="1.2"/><path d="M1 2 L5 5.5 L9 2" fill="none" stroke="var(--royal-blue)" stroke-width="1.2"/></svg>
        info@tkale-studio.example
      </li>
      <li class="contact__item">
        <svg class="contact__icon" viewBox="0 0 10 10"><rect x="1" y="1" width="8" height="8" fill="var(--royal-blue)"/></svg>
        @t.kalestudio
      </li>
      <li class="contact__item">
        <svg class="contact__icon" viewBox="0 0 10 10"><circle cx="5" cy="5" r="4.2" fill="none" stroke="var(--royal-blue)" stroke-width="1.2"/><path d="M0.8 5 H9.2 M5 0.8 Q2.5 5 5 9.2 M5 0.8 Q7.5 5 5 9.2" fill="none" stroke="var(--royal-blue)" stroke-width="0.9"/></svg>
        www.tkale-studio.example
      </li>
    </ul>
  </section>

  <section class="card card--back" aria-label="Brand side">
    <span class="wordmark__dot"></span>
    <span class="wordmark__name">T. Kale Photography</span>
  </section>
</main>
</body>
</html>
```